Pulp&Vine

We need a new menu design for a juice shop called pulp&Vine

Industry/Entity Type

Shop

Colors
9bcb3c
ffcf3e
ffffff
f04a51

Requirements
Must have
• we want winter version and summer version must have focus on hot drinks and chocolate and there must be images to bring the attention to these items and same as for the summer version, we need new design and fresh look.
• this is our instagram account : pulpandvine.lb
• you can find pictures and use them or you can download similar pictures with higher resolution.
• and we need to add Turkish coffee 2000LL to the menu.
• i need the green and orange colors to be the main ones.
• size of menu : A4

```html
<!DOCTYPE html>
<html lang="en">
<head>
<meta charset="UTF-8">
<title>Pulp&amp;Vine — Winter Drinks Menu</title>
<link href="https://fonts.googleapis.com/css2?family=Patua+One&family=Arimo:wght@400;700&display=swap" rel="stylesheet">
<style>
  :root {
    --bg-light: #f2c65a;
    --bg-mid: #e7b449;
    --bg-dark: #d59a34;
    --brown: #6b3a1f;
    --green: #9bcb3c;
    --orange: #ffcf3e;
    --red: #f04a51;
    --white: #ffffff;
    --choc-dark: #4a2412;
    --choc-mid: #7a4422;
    --choc-light: #a86b3e;
    --juice: #f3a52a;
  }
  html, body {
    margin: 0;
    padding: 0;
    width: 853px;
    height: 1200px;
    overflow: hidden;
  }
  .menu {
    position: relative;
    width: 853px;
    height: 1200px;
    overflow: hidden;
    background: radial-gradient(ellipse at 45% 45%, var(--bg-light) 0%, var(--bg-mid) 55%, var(--bg-dark) 100%);
    font-family: "Arimo", Arial, sans-serif;
  }
  .brand {
    position: absolute;
    left: 80px;
    top: 88px;
    display: flex;
    align-items: center;
    gap: 10px;
  }
  .brand-dot {
    width: 22px;
    height: 22px;
    border-radius: 50%;
    background: var(--green);
  }
  .brand-name {
    font-weight: 700;
    font-size: 30px;
    color: var(--white);
  }
  .photo {
    position: absolute;
  }
  .photo-chocolate-splash {
    left: 413px;
    top: 0;
    width: 440px;
    height: 330px;
    background: radial-gradient(ellipse 55% 60% at 50% 35%, var(--choc-light) 0%, var(--choc-mid) 40%, var(--choc-dark) 70%, rgba(74,36,18,0) 100%);
  }
  .photo-glass {
    left: 0;
    top: 620px;
    width: 570px;
    height: 580px;
    background: radial-gradient(ellipse 60% 75% at 30% 50%, var(--choc-mid) 0%, var(--choc-dark) 35%, rgba(122,68,34,0.8) 55%, rgba(243,165,42,0.7) 75%, rgba(213,154,52,0) 100%);
  }
  .title {
    position: absolute;
    margin: 0;
    font-family: "Patua One", Georgia, serif;
    font-weight: 400;
    color: var(--brown);
    line-height: 0.9;
    letter-spacing: 3px;
  }
  .title-winter {
    left: 22px;
    top: 222px;
    font-size: 80px;
  }
  .title-hot {
    left: 424px;
    top: 512px;
    font-size: 52px;
    letter-spacing: 4px;
  }
  .stroke {
    position: absolute;
    height: 14px;
    border-radius: 8px 3px 9px 4px;
    background: var(--green);
  }
  .stroke-winter { left: 22px; top: 366px; width: 320px; }
  .stroke-hot { left: 424px; top: 574px; width: 260px; height: 11px; }
  .item-list {
    position: absolute;
    margin: 0;
    padding: 0;
    list-style: none;
    font-size: 15px;
    color: var(--white);
  }
  .item-list li {
    display: flex;
    align-items: flex-end;
    line-height: 1.35;
    margin-bottom: 8px;
  }
  .item-name { flex: 0 0 auto; }
  .item-dots {
    flex: 1 1 auto;
    border-bottom: 1px dotted rgba(255,255,255,0.7);
    margin: 0 4px 5px;
  }
  .item-price {
    color: var(--red);
    font-weight: 700;
  }
  .list-winter { left: 24px; top: 404px; width: 310px; }
  .list-hot { left: 424px; top: 604px; width: 280px; }
  .social {
    position: absolute;
    right: 48px;
    bottom: 40px;
    font-size: 16px;
    font-weight: 700;
    color: var(--white);
  }
</style>
</head>
<body>
<main class="menu">
  <div class="brand">
    <span class="brand-dot"></span>
    <span class="brand-name">Pulp&amp;Vine</span>
  </div>

  <div class="photo photo-chocolate-splash" role="img" aria-label="Photo of a chocolate drink splashing with chocolate pieces"></div>
  <div class="photo photo-glass" role="img" aria-label="Photo of a glass of chocolate drink with strawberries and an orange juice splash"></div>

  <h1 class="title title-winter">WINTER<br>DRINKS</h1>
  <span class="stroke stroke-winter"></span>

  <ul class="item-list list-winter">
    <li><span class="item-name">Chocolate Shake</span><span class="item-dots"></span><span class="item-price">$0.00</span></li>
    <li><span class="item-name">Chikko - Choco</span><span class="item-dots"></span><span class="item-price">$0.00</span></li>
    <li><span class="item-name">Warm Bourbon Cider</span><span class="item-dots"></span><span class="item-price">$0.00</span></li>
    <li><span class="item-name">Cranberry Apple Cider<br>Punch</span><span class="item-dots"></span><span class="item-price">$0.00</span></li>
  </ul>

  <h2 class="title title-hot">HOT DRINKS</h2>
  <span class="stroke stroke-hot"></span>

  <ul class="item-list list-hot">
    <li><span class="item-name">Hot Coco</span><span class="item-dots"></span><span class="item-price">$0.00</span></li>
    <li><span class="item-name">Double Hot Chocolate</span><span class="item-dots"></span><span class="item-price">$0.00</span></li>
    <li><span class="item-name">Cafe Mocha</span><span class="item-dots"></span><span class="item-price">$0.00</span></li>
    <li><span class="item-name">Hot Holiday Apple<br>Cider</span><span class="item-dots"></span><span class="item-price">$0.00</span></li>
    <li><span class="item-name">Mint White Hot<br>Chocolate</span><span class="item-dots"></span><span class="item-price">$0.00</span></li>
    <li><span class="item-name">Snickerdoodle Hot<br>Cocoa</span><span class="item-dots"></span><span class="item-price">$0.00</span></li>
    <li><span class="item-name">Turkish Coffee</span><span class="item-dots"></span><span class="item-price">2000LL</span></li>
  </ul>

  <p class="social">Instagram: pulpandvine.lb</p>
</main>
</body>
</html>
```